Kettle Past Noon - Book cover for collection of odd short stories

We need a book cover for ebook and print versions for an anthology of short stories. The title "Kettle Past Noon" relates to stories with something odd or not-quite-right about them. The attached photo is an example of a carpenter level, the idea is the level would appear perfectly level, but the bubble would be off-center. "Stories by: Moira Tesslund, Janet Orloff, Rob T. Vessey, Author, Author". Other creative elements could be wildly improbable things, e.g. pig's flying, hell freezing, etc. We prefer an uncluttered cover, however. Licenses included or unnecessary, delivery files must be fully compatible with Adobe Illustrator, with all layers intact.

Target Market(s)

People who like short stories with odd overtones or twist endings.

Industry/Entity Type

Book Publisher

Font styles to use
Serif

Colors

Designer to choose colors to be used in the design.

Requirements
Must have
• Incorporation of the concept, Kettle Past Noon
Nice to have
• Other ways to show the same meaning

```html
<!DOCTYPE html>
<html lang="en">
<head>
<meta charset="utf-8">
<title>Kettle Past Noon — Book Cover</title>
<link rel="stylesheet" href="https://fonts.googleapis.com/css2?family=Cinzel:wght@900&family=Open+Sans:wght@400;700&display=swap">
<style>
  :root {
    --paper: #ffffff;
    --teal: #1fb3b6;
    --teal-light: #3cc9c9;
    --teal-dark: #0e7f85;
    --title: #ffffff;
    --title-shade: #dcdcdc;
    --title-shadow: #0a5e63;
    --level-yellow: #f2c12e;
    --level-deep: #d99e13;
    --byline: #ffffff;
  }
  * { margin: 0; padding: 0; box-sizing: border-box; }
  html, body { width: 821px; height: 1200px; overflow: hidden; background: var(--paper); }
  .cover {
    position: relative;
    width: 821px;
    height: 1200px;
    background: var(--paper);
    overflow: hidden;
  }
  .cover-panel {
    position: absolute;
    left: 22px; top: 22px;
    width: 778px; height: 1148px;
    background: radial-gradient(ellipse at 50% 45%, var(--teal-light) 0%, var(--teal) 55%, var(--teal-dark) 120%);
  }
  .title-line {
    position: absolute;
    left: 0; width: 821px;
    text-align: center;
    font-family: "Cinzel", serif;
    font-weight: 900;
    font-size: 176px;
    line-height: 1;
    letter-spacing: 2px;
    color: var(--title);
    background: linear-gradient(180deg, var(--title) 45%, var(--title-shade) 100%);
    -webkit-background-clip: text;
    background-clip: text;
    -webkit-text-fill-color: transparent;
    filter: drop-shadow(-4px 5px 0 var(--title-shadow));
  }
  .title-line--first { top: 100px; }
  .title-line--second { top: 268px; }
  .title-line--third { top: 704px; }
  .spirit-level {
    position: absolute;
    left: 0; top: 446px;
    width: 821px; height: 248px;
    background: linear-gradient(180deg, var(--level-yellow) 0%, #f6cf48 45%, var(--level-deep) 100%);
  }
  .byline {
    position: absolute;
    left: 0; top: 982px;
    width: 821px;
    text-align: center;
    color: var(--byline);
    font-family: "Open Sans", sans-serif;
    text-transform: uppercase;
  }
  .byline-label {
    font-weight: 400;
    font-size: 19px;
    letter-spacing: 0.5px;
    margin-bottom: 8px;
  }
  .byline-authors {
    font-weight: 700;
    font-size: 27px;
    line-height: 38px;
    letter-spacing: 0.3px;
  }
</style>
</head>
<body>
  <main class="cover">
    <div class="cover-panel"></div>

    <h1 class="book-title">
      <span class="title-line title-line--first">KETTLE</span>
      <span class="title-line title-line--second">PAST</span>
      <span class="title-line title-line--third">NOON</span>
    </h1>

    <div class="spirit-level" role="img" aria-label="Photograph of a yellow carpenter's spirit level with ruler markings and three green vials, the bubbles resting off-centre"></div>

    <div class="byline">
      <p class="byline-label">Stories by</p>
      <p class="byline-authors">Moira Tesslund, Janet Orloff,<br>Rob T. Vessey, Lou Brennick &amp; Others</p>
    </div>
  </main>
</body>
</html>
```